Velmor Crest - Advanced Skincare and undetectable Makeup for Men

We are in need of a professional webpage for our company Velmor Crest. We help every man feel his best by looking his best. Inspired by the myth of Adonis, we offer makeup and skincare products along with education upon their use. Our mission is to celebrate masculinity in all of its forms, regardless of age, race, sexual orientation, or assigned gender at birth.

The webpage would serve as our online store, as a place where our clients can learn about our brand, view our "How-to" video tutorials, and get product information. An online blog will also be hosted in order to keep clients up to date with news, updates, media mentions, etc.

The color schemes that we use are mostly Black and Gold, with Red accents. please keep in mind that this is a men's cosmetics line, and therefore should read powerful, sexy, confident and bold - all with a high end look and feel.

Think along the lines of brands like Dirk Halvan, QBN, Belcuzzi, etc.

our logo is included in the files attached. images and copy will be added in at a later time; hence, general images that fit the feel and filler text is encouraged.

The products to be sold include:
a face cleanser in a pump dispenser bottle (1 size)
a mask in a round jar container (1 size)
a moisturizer in a pump container 1 size)
a concealer in a click pen with a brush applicator (3 shades)
a liquid liner pen (4 shades)
a contouring palette (2 shade options)
a setting spray (single option)

Target Market(s)

Millennial Men

Industry/Entity Type

Beauty

Number of Pages Required

5+ page

Font styles to use
Serif

Colors
ec1f27
000000
faa54b

Requirements
Must have
• ur essential requirements are:
• 1) a stunning and engaging landing page that truly captures the ideals of sexuality, boldness and confidence.
• 2) an interactive and engaging online store that is easy to update / add product / information to.
• 3) Product pages supporting various toggling images of the product, a shade selection option, ingredient information, usage instructions, pricing, and a link to a "how to video" unique to each individual product.
• 4) dedicated space where all of the tutorials can be organized together
• 5) an organized Blog section, that would include a segment for a Q&A section for us to update as the brand grows, ongoing contests (that would be easily hidden if there are no contests running at the moment) as well as general news and updates segment.
• 6) an "about us" page, where our customers are able to learn about our story, inspirations, humanitarian efforts and philosophies in product contents and purity.
• 7) a contact us page, which would include social media links, contact email and telephone number as well as physical address to be updated upon launch.
• 8) discrete privacy policy, terms of use, and return policy links available at the bottom of every page
Nice to have
• 1) A posting forum where clients could post their looks using our products, or maybe a live stream of our Pictoloop account.
• 2) a member sign in page so that we can collect and store customer information for faster check out, keep track of purchases attached to their email address (future loyalty program plans) and maintain an email database for email notifications and the such.

```html
<!DOCTYPE html>
<html lang="en">
<head>
<meta charset="utf-8">
<title>Velmor Crest – Home Page Concepts</title>
<link href="https://fonts.googleapis.com/css2?family=Roboto+Slab:wght@300;400;700&display=swap" rel="stylesheet">
<style>
:root{
  --ink:#1b1b1b;
  --gold:#c59a5c;
  --red:#c8102e;
  --text:#333;
  --muted:#8a8a8a;
  --line:#e3e3e3;
  --paper:#ffffff;
}
*{box-sizing:border-box;margin:0;padding:0}
html,body{width:819px;height:1200px;overflow:hidden;background:var(--paper)}
body{font-family:"Roboto Slab",serif;color:var(--text)}
.canvas{position:relative;width:819px;height:1200px;overflow:hidden}
.stage{position:absolute;left:4px;top:0;width:1013px;height:1500px;transform:scale(.8);transform-origin:0 0}
.page{position:absolute;width:438px;height:1426px;background:var(--paper);box-shadow:0 0 6px rgba(0,0,0,.18);overflow:hidden}
.page--light{left:51px;top:37px}
.page--dark{left:524px;top:36px}

/* header */
.site-header{position:relative;height:64px;background:var(--ink)}
.brand{position:absolute;left:24px;top:8px;width:84px;text-align:center;color:var(--gold)}
.brand__mark{display:block;width:18px;height:18px;margin:0 auto 5px;border:1.5px solid var(--gold)}
.brand__name{display:block;font-size:6px;letter-spacing:2.4px;text-transform:uppercase;white-space:nowrap}
.utility{position:absolute;right:20px;top:5px;font-size:4.5px;color:#8d8d8d;display:flex;gap:12px}
.account{position:absolute;right:22px;top:28px;font-size:4.6px;color:#ddd;display:flex;gap:12px;align-items:center}
.account__cart{color:var(--gold);display:flex;align-items:center;gap:3px}
.account__cart i{width:8px;height:6px;border:1px solid #aaa;border-radius:1px;display:inline-block}
.main-nav{position:absolute;left:24px;top:52px;width:374px;height:20px;background:var(--paper);border:1px solid var(--line);display:flex;align-items:center;padding-left:18px;gap:15px;font-size:4.6px;color:#333;z-index:2;white-space:nowrap}
.main-nav .is-active{color:var(--gold)}
.search{margin-left:auto;margin-right:6px;width:96px;height:11px;border:1px solid var(--line);font-size:4.2px;color:#aaa;padding:2px 5px;position:relative}
.search::after{content:"";position:absolute;right:6px;top:2px;width:4px;height:4px;border:1px solid #777;border-radius:50%}

/* hero */
.hero{position:relative;height:213px;overflow:hidden}
.page--light .hero{background:linear-gradient(90deg,#f6f4f1 0%,#ecebe8 55%,#dcd8d4 100%)}
.page--dark .hero{background:linear-gradient(90deg,#1d1d1d 0%,#262626 55%,#3a3330 100%)}
.hero__photo{position:absolute;right:0;top:0;width:230px;height:213px}
.page--light .hero__photo{background:linear-gradient(120deg,#e9e6e2 0%,#b8a39a 40%,#5a2a2a 60%,#1f1f25 100%)}
.page--dark .hero__photo{background:linear-gradient(110deg,#2a2624 0%,#8c6c5a 40%,#d8d2cc 60%,#6e4a3e 85%,#241c1a 100%)}
.hero__copy{position:absolute;left:40px;top:66px;width:150px}
.hero__title{color:var(--red);font-size:15px;font-weight:400;line-height:1;white-space:nowrap}
.hero__sub{font-size:6.2px;letter-spacing:2px;margin-top:3px;color:#222;text-transform:uppercase;white-space:nowrap}
.hero__text{font-size:4.8px;line-height:1.6;color:#777;margin-top:6px;width:118px}
.page--dark .hero__text{color:#999;margin-top:12px}
.btn-gold{display:inline-block;background:var(--gold);color:#fff;font-size:4.2px;padding:3px 10px;text-transform:uppercase;margin-top:15px}
.hero__dots{position:absolute;left:212px;bottom:17px;display:flex;gap:2px}
.hero__dots i{width:4px;height:2px;background:#bbb}
.hero__dots i:first-child{background:var(--gold)}

/* section heads */
.section-title{text-align:center;font-size:10px;letter-spacing:.6px;color:#222;font-weight:400;text-transform:uppercase}
.section-title::after{content:"";display:block;width:11px;height:1.5px;background:var(--gold);margin:8px auto 0}

/* products */
.products{height:346px;padding-top:32px}
.product-grid{display:grid;grid-template-columns:repeat(3,108px);justify-content:center;row-gap:14px;margin-top:18px}
.product{text-align:center}
.product__img{height:72px;margin:0 auto 6px;border-radius:2px}
.product__img--spray{width:40px;background:linear-gradient(180deg,#c9a86a 0 28%,#1c1c1c 28% 100%)}
.product__img--pen{width:62px;height:14px;margin:28px auto 36px;background:linear-gradient(90deg,#1c1c1c 80%,#c9a86a 80%)}
.product__img--palette{width:66px;height:34px;margin:20px auto 24px;background:linear-gradient(135deg,#e8e8e8 0 40%,#b5763e 40% 60%,#1c1c1c 60%)}
.product__name{font-size:5.6px;color:#222;white-space:nowrap}
.product__meta{font-size:3.9px;color:var(--muted);line-height:1.7;margin-top:3px}
.product__meta b{display:inline-block;width:4px;height:4px;border-radius:50%;background:#e08a8a;vertical-align:middle;margin-left:1px}
.product__meta b.g{background:#8b7a60}
.product__rating{font-size:4px;color:#bbb;letter-spacing:1px;margin-top:2px}

/* founder */
.founder{position:relative;height:153px;background:linear-gradient(90deg,#c3965a 0%,#b58a52 50%,#c59d66 100%)}
.founder__copy{position:absolute;left:63px;top:36px;width:195px;color:#fff}
.founder__title{font-size:9.5px;font-weight:400;line-height:1;text-transform:uppercase}
.founder__text{font-size:4.5px;line-height:1.95;margin-top:6px}
.founder__more{font-size:4.2px;margin-top:10px;font-style:italic;text-transform:uppercase}
.founder__photo{position:absolute;left:279px;top:35px;width:126px;height:118px;background:linear-gradient(160deg,#4a5b66 0%,#6d7d84 50%,#3e5660 100%)}

/* clients */
.clients{height:319px;padding-top:38px}
.client-grid{display:grid;grid-template-columns:repeat(3,98px);gap:11px;justify-content:center;margin-top:15px}
.client{position:relative;height:86px}
.client--a{background:linear-gradient(135deg,#b99d7b,#e2c9ad)}
.client--b{background:linear-gradient(135deg,#7d8a95,#e6d2c2)}
.client--c{background:linear-gradient(135deg,#f4f4f4,#d6c8b8)}
.client__zoom{position:absolute;right:4px;top:4px;width:10px;height:10px;background:var(--gold);opacity:.85}
.btn-outline{display:block;width:85px;margin:31px auto 0;border:1px solid #555;font-size:4.2px;text-align:center;padding:6px 0;text-transform:uppercase}

/* newsletter */
.newsletter{position:relative;height:215px;background:linear-gradient(180deg,#ffffff 0%,#e9ece8 22%,#8d9175 48%,#5e6142 68%,#7e6a3d 100%);text-align:center;color:#fff}
.newsletter__title{position:absolute;top:102px;width:100%;font-size:15px;font-weight:400;letter-spacing:.5px}
.newsletter__text{position:absolute;top:124px;left:120px;width:198px;font-size:5px;line-height:1.9}
.newsletter__form{position:absolute;left:87px;top:157px;display:flex}
.newsletter__input{width:209px;height:21px;background:#fff;color:#999;font-size:4.8px;text-align:left;padding:7px 16px}
.newsletter__btn{width:56px;height:21px;background:var(--gold);font-size:4.4px;padding-top:8px;text-transform:uppercase}

/* footer */
.site-footer{height:95px;text-align:center;padding-top:12px}
.site-footer .brand__mark{border-color:#333;margin:0 auto 6px}
.site-footer .brand__name{color:#333;font-size:5.2px}
.footer-links{display:flex;justify-content:center;gap:12px;font-size:4.2px;margin-top:13px;color:#444}
.social{display:flex;justify-content:center;gap:6px;margin-top:8px}
.social i{width:14px;height:14px;border-radius:50%;background:#b5b5b5}
.legal-bar{height:21px;background:var(--ink);color:#555;font-size:3.8px;text-align:center;padding-top:8px}
</style>
</head>
<body>
<div class="canvas">
<div class="stage">

<main class="page page--light">
  <header class="site-header">
    <div class="brand"><span class="brand__mark"></span><span class="brand__name">Velmor Crest</span></div>
    <div class="utility"><span>Login</span><span>Register</span></div>
    <div class="account"><span>My Account</span><span>Checkout</span><span>My Wishlist</span><span class="account__cart"><i></i>0 item(s) - £0.00</span></div>
    <nav class="main-nav"><span class="is-active">Home</span><span>Products</span><span>About Us</span><span>Shop</span><span>Deals</span><span>Blog</span><span>Contact Us</span><span class="search">Search...</span></nav>
  </header>
  <section class="hero">
    <div class="hero__photo" role="img" aria-label="Campaign photo of a couple in evening wear"></div>
    <div class="hero__copy">
      <h1 class="hero__title">LOREM LIPSUM</h1>
      <p class="hero__sub">Is simply a dummy text</p>
      <p class="hero__text">Contrary to popular belief is not simply random text.</p>
      <span class="btn-gold">Buy now</span>
    </div>
    <div class="hero__dots"><i></i><i></i><i></i></div>
  </section>
  <section class="products">
    <h2 class="section-title">Our Products</h2>
    <div class="product-grid">
      <div class="product"><div class="product__img product__img--spray" role="img" aria-label="Setting spray bottle"></div><p class="product__name">Ironset Mist</p><p class="product__meta">Colors: N/A<br>Price: $28.00</p><p class="product__rating">★★★</p></div>
      <div class="product"><div class="product__img product__img--pen" role="img" aria-label="Concealer click pen"></div><p class="product__name">Dusk Concealer</p><p class="product__meta">Colors: <b></b><b></b><b></b><br>Price: $26.00</p><p class="product__rating">★★★</p></div>
      <div class="product"><div class="product__img product__img--palette" role="img" aria-label="Contour palette"></div><p class="product__name">Sculpt Palette</p><p class="product__meta">Colors: <b class="g"></b><b class="g"></b><br>Price: $50.00</p><p class="product__rating">★★★</p></div>
      <div class="product"><div class="product__img product__img--palette" role="img" aria-label="Contour palette"></div><p class="product__name">Sculpt Palette</p><p class="product__meta">Colors: <b class="g"></b><b class="g"></b><br>Price: $50.00</p><p class="product__rating">★★★</p></div>
      <div class="product"><div class="product__img product__img--spray" role="img" aria-label="Setting spray bottle"></div><p class="product__name">Ironset Mist</p><p class="product__meta">Colors: N/A<br>Price: $28.00</p><p class="product__rating">★★★</p></div>
      <div class="product"><div class="product__img product__img--pen" role="img" aria-label="Concealer click pen"></div><p class="product__name">Dusk Concealer</p><p class="product__meta">Colors: <b></b><b></b><b></b><br>Price: $26.00</p><p class="product__rating">★★★</p></div>
    </div>
  </section>
  <section class="founder">
    <div class="founder__copy">
      <h2 class="founder__title">A warm welcome<br>from our founder</h2>
      <p class="founder__text">It is a long established fact that a reader will be distracted by the readable content of a page when looking at its layout. The point of using Lorem Ipsum is that it has a Content here, content here', making it look like readable English.</p>
      <p class="founder__more">› Read more</p>
    </div>
    <div class="founder__photo" role="img" aria-label="Portrait of the founder in a plaid shirt"></div>
  </section>
  <section class="clients">
    <h2 class="section-title">Happy Clients</h2>
    <div class="client-grid">
      <div class="client client--a" role="img" aria-label="Client photo"><span class="client__zoom"></span></div>
      <div class="client client--b" role="img" aria-label="Client photo"><span class="client__zoom"></span></div>
      <div class="client client--c" role="img" aria-label="Client photo"><span class="client__zoom"></span></div>
      <div class="client client--a" role="img" aria-label="Client photo"><span class="client__zoom"></span></div>
      <div class="client client--b" role="img" aria-label="Client photo"><span class="client__zoom"></span></div>
      <div class="client client--c" role="img" aria-label="Client photo"><span class="client__zoom"></span></div>
    </div>
    <span class="btn-outline">Get social with us</span>
  </section>
  <section class="newsletter" role="img" aria-label="Mountain valley landscape">
    <h2 class="newsletter__title">Sign-up Newsletter</h2>
    <p class="newsletter__text">Lorem Ipsum is simply dummy text of the printing and typesetting industry</p>
    <div class="newsletter__form"><span class="newsletter__input">Enter Your Email Address</span><span class="newsletter__btn">Subscribe</span></div>
  </section>
  <footer class="site-footer">
    <span class="brand__mark"></span><span class="brand__name">Velmor Crest</span>
    <div class="footer-links"><span>About Us</span><span>Our Products</span><span>Frequently Asked Questions</span><span>Blog</span><span>Contact Us</span></div>
    <div class="social"><i></i><i></i><i></i></div>
  </footer>
  <div class="legal-bar">© 2018 Velmor Crest. All Rights Reserved</div>
</main>

<main class="page page--dark">
  <header class="site-header">
    <div class="brand"><span class="brand__mark"></span><span class="brand__name">Velmor Crest</span></div>
    <div class="utility"><span>Login</span><span>Register</span></div>
    <div class="account"><span>My Account</span><span>Checkout</span><span>My Wishlist</span><span class="account__cart"><i></i>0 item(s) - £0.00</span></div>
    <nav class="main-nav"><span class="is-active">Home</span><span>Products</span><span>About Us</span><span>Shop</span><span>Deals</span><span>Blog</span><span>Contact Us</span><span class="search">Search...</span></nav>
  </header>
  <section class="hero">
    <div class="hero__photo" role="img" aria-label="Campaign photo of a tattooed couple"></div>
    <div class="hero__copy">
      <h1 class="hero__title">LOREM LIPSUM</h1>
      <p class="hero__text">Contrary to popular belief is not simply random text.</p>
      <span class="btn-gold">Buy now</span>
    </div>
    <div class="hero__dots"><i></i><i></i><i></i></div>
  </section>
  <section class="products">
    <h2 class="section-title">Our Products</h2>
    <div class="product-grid">
      <div class="product"><div class="product__img product__img--spray" role="img" aria-label="Setting spray bottle"></div><p class="product__name">Ironset Mist</p><p class="product__meta">Colors: N/A<br>Price: $28.00</p><p class="product__rating">★★★</p></div>
      <div class="product"><div class="product__img product__img--pen" role="img" aria-label="Concealer click pen"></div><p class="product__name">Dusk Concealer</p><p class="product__meta">Colors: <b></b><b></b><b></b><br>Price: $26.00</p><p class="product__rating">★★★</p></div>
      <div class="product"><div class="product__img product__img--palette" role="img" aria-label="Contour palette"></div><p class="product__name">Sculpt Palette</p><p class="product__meta">Colors: <b class="g"></b><b class="g"></b><br>Price: $50.00</p><p class="product__rating">★★★</p></div>
      <div class="product"><div class="product__img product__img--palette" role="img" aria-label="Contour palette"></div><p class="product__name">Sculpt Palette</p><p class="product__meta">Colors: <b class="g"></b><b class="g"></b><br>Price: $50.00</p><p class="product__rating">★★★</p></div>
      <div class="product"><div class="product__img product__img--spray" role="img" aria-label="Setting spray bottle"></div><p class="product__name">Ironset Mist</p><p class="product__meta">Colors: N/A<br>Price: $28.00</p><p class="product__rating">★★★</p></div>
      <div class="product"><div class="product__img product__img--pen" role="img" aria-label="Concealer click pen"></div><p class="product__name">Dusk Concealer</p><p class="product__meta">Colors: <b></b><b></b><b></b><br>Price: $26.00</p><p class="product__rating">★★★</p></div>
    </div>
  </section>
  <section class="founder">
    <div class="founder__copy">
      <h2 class="founder__title">A warm welcome<br>from our founder</h2>
      <p class="founder__text">It is a long established fact that a reader will be distracted by the readable content of a page when looking at its layout. The point of using Lorem Ipsum is that it has a Content here, content here', making it look like readable English.</p>
      <p class="founder__more">› Read more</p>
    </div>
    <div class="founder__photo" role="img" aria-label="Portrait of the founder in a plaid shirt"></div>
  </section>
  <section class="clients">
    <h2 class="section-title">Happy Clients</h2>
    <div class="client-grid">
      <div class="client client--a" role="img" aria-label="Client photo"><span class="client__zoom"></span></div>
      <div class="client client--b" role="img" aria-label="Client photo"><span class="client__zoom"></span></div>
      <div class="client client--c" role="img" aria-label="Client photo"><span class="client__zoom"></span></div>
      <div class="client client--a" role="img" aria-label="Client photo"><span class="client__zoom"></span></div>
      <div class="client client--b" role="img" aria-label="Client photo"><span class="client__zoom"></span></div>
      <div class="client client--c" role="img" aria-label="Client photo"><span class="client__zoom"></span></div>
    </div>
    <span class="btn-outline">Get social with us</span>
  </section>
  <section class="newsletter" role="img" aria-label="Mountain valley landscape">
    <h2 class="newsletter__title">Sign-up Newsletter</h2>
    <p class="newsletter__text">Lorem Ipsum is simply dummy text of the printing and typesetting industry</p>
    <div class="newsletter__form"><span class="newsletter__input">Enter Your Email Address</span><span class="newsletter__btn">Subscribe</span></div>
  </section>
  <footer class="site-footer">
    <span class="brand__mark"></span><span class="brand__name">Velmor Crest</span>
    <div class="footer-links"><span>About Us</span><span>Our Products</span><span>Frequently Asked Questions</span><span>Blog</span><span>Contact Us</span></div>
    <div class="social"><i></i><i></i><i></i></div>
  </footer>
  <div class="legal-bar">© 2018 Velmor Crest. All Rights Reserved</div>
</main>

</div>
</div>
</body>
</html>
```